Need CATCHY/VIVID Banner design for my new UTV/ATV/Off Road Vehicle turn signal/lighting company

I need a banner ad designed so I can advertise on several different ATV (all terrain vehicle), UTV (Utility Vehicles), Golf Cart and Off-Road Vehicle forums. Ads need to be very catchy and produce a call to action. Action is getting hits to my website. Our main business is selling turn signal kits to make your side by side or your ATV/UTV street legal, as some states now allow you to drive these on public roads if you have the following items: Turn Signals, Horn, Lighted license plate bracket, headlights and brake lights. We sell all of these items for just about any model vehicle out there. Our call to action for this banner would be to get more website visits.

Target Market(s)

Off-road/outdoor enthusiasts,

Industry/Entity Type

Car Accessorie

Font styles to use
Sans Serif

Requirements
Must have
• Ad size need to be either 728x90 or 300x250. Colorful ad with an off-road vehicle integrated to the design (think UTV, side-by-side, etc.
Nice to have
• Nice to haves would be anything that makes this banner ad stand out on very boring web pages.
Should not have
• anything dull

```html
<!DOCTYPE html>
<html lang="en">
<head>
<meta charset="utf-8">
<title>Trailwink – ATV &amp; UTV Signal Lighting</title>
<link rel="stylesheet" href="https://fonts.googleapis.com/css2?family=Montserrat:wght@700;800;900&display=swap">
<style>
  :root {
    --navy: #1b1c2b;
    --navy-deep: #14151f;
    --maroon: #3a1823;
    --red: #e5231f;
    --orange: #f26a1b;
    --amber: #f9a51a;
    --yellow: #f7c21c;
    --white: #ffffff;
    --icon-ink: #1b1c2b;
    --sky: #a9bfd2;
    --haze: #cbbfae;
    --rock-light: #c49a6c;
    --rock-mid: #9c7048;
    --rock-dark: #5e4030;
  }
  * { margin: 0; padding: 0; box-sizing: border-box; }
  html, body { width: 1200px; height: 1000px; overflow: hidden; background: var(--navy); }
  .banner {
    position: relative;
    width: 1200px;
    height: 1000px;
    overflow: hidden;
    font-family: "Montserrat", Arial, sans-serif;
    color: var(--white);
  }
  .hero-photo {
    position: absolute; inset: 0;
    background:
      radial-gradient(ellipse 320px 380px at 960px 520px, rgba(30,24,24,0.85) 0%, rgba(60,30,28,0.6) 55%, rgba(0,0,0,0) 100%),
      linear-gradient(180deg, var(--sky) 0%, var(--haze) 14%, var(--rock-light) 34%, var(--rock-mid) 62%, var(--rock-dark) 100%);
  }
  .shapes { position: absolute; inset: 0; }
  .brand {
    position: absolute; left: 60px; top: 70px; width: 484px;
    display: flex; align-items: center; justify-content: center; gap: 16px;
  }
  .brand-dot { width: 32px; height: 32px; border-radius: 50%; background: var(--red); }
  .brand-name { font-size: 60px; font-weight: 800; letter-spacing: 1px; color: var(--red); }
  .tagline {
    position: absolute; left: 56px; top: 204px; width: 492px;
    text-align: center; font-weight: 800; text-transform: uppercase; line-height: 1.1;
  }
  .tagline-main { display: block; font-size: 41px; letter-spacing: -0.5px; }
  .tagline-sub { display: block; font-size: 25.5px; letter-spacing: 0; }
  .headline {
    position: absolute; left: 50px; top: 340px;
    font-weight: 800; font-size: 92px; line-height: 1.02; text-transform: uppercase; letter-spacing: 1px;
  }
  .subhead {
    position: absolute; left: 58px; top: 536px;
    font-size: 42px; font-weight: 800; color: var(--red); text-transform: uppercase; letter-spacing: 0.5px;
  }
  .vehicle-photo {
    position: absolute; left: 30px; top: 640px; width: 480px; height: 330px;
    border-radius: 60px 60px 40px 40px;
    background:
      radial-gradient(ellipse 150px 90px at 270px 170px, rgba(229,35,31,0.55) 0%, rgba(229,35,31,0) 100%),
      radial-gradient(ellipse 240px 160px at 240px 180px, #a3a19c 0%, #5a5a5c 55%, rgba(27,28,43,0) 100%);
  }
  .feature-icon {
    position: absolute; width: 140px; height: 140px; border-radius: 50%;
    background: var(--yellow);
    display: flex; align-items: center; justify-content: center;
  }
  .feature-icon svg { width: 84px; height: 84px; }
  .icon-turn  { left: 658px; top: 164px; }
  .icon-brake { left: 582px; top: 340px; }
  .icon-head  { left: 512px; top: 486px; }
  .icon-horn  { left: 430px; top: 638px; }
</style>
</head>
<body>
<main class="banner">
  <div class="hero-photo" role="img" aria-label="Red and black UTV side-by-side climbing desert rocks under a mountain sky"></div>

  <svg class="shapes" viewBox="0 0 1200 1000" width="1200" height="1000" aria-hidden="true">
    <polygon points="760,0 860,0 820,110" fill="var(--amber)"/>
    <polygon points="800,0 842,0 432,1000 392,1000" fill="var(--red)"/>
    <polygon points="0,0 800,0 392,1000 0,1000" fill="var(--navy)"/>
    <polygon points="0,60 160,0 330,0 0,330" fill="var(--maroon)" opacity="0.8"/>
  </svg>

  <div class="brand">
    <span class="brand-dot"></span>
    <span class="brand-name">TRAILWINK</span>
  </div>

  <p class="tagline">
    <span class="tagline-main">Turn Signal Kits</span>
    <span class="tagline-sub">&amp; Lighting Accessories</span>
  </p>

  <h1 class="headline">ATV&amp; UTV<br>Vehicle</h1>
  <p class="subhead">Signal Lighting</p>

  <div class="vehicle-photo" role="img" aria-label="Grey and red sport UTV with roll cage, front three-quarter view"></div>

  <div class="feature-icon icon-turn" aria-label="Turn signals">
    <svg viewBox="0 0 84 84" fill="none" stroke="var(--icon-ink)" stroke-width="6" stroke-linecap="round" stroke-linejoin="round">
      <path d="M8 42 L22 28 M8 42 L22 56 M8 42 H34"/>
      <path d="M76 42 L62 28 M76 42 L62 56 M76 42 H50"/>
    </svg>
  </div>
  <div class="feature-icon icon-brake" aria-label="Brake lights">
    <svg viewBox="0 0 84 84" fill="none" stroke="var(--icon-ink)" stroke-width="6" stroke-linecap="round">
      <circle cx="42" cy="42" r="20"/>
      <path d="M18 22 A30 30 0 0 0 18 62 M66 22 A30 30 0 0 1 66 62"/>
      <path d="M42 32 V44"/>
      <circle cx="42" cy="52" r="1.5" fill="var(--icon-ink)"/>
    </svg>
  </div>
  <div class="feature-icon icon-head" aria-label="Headlights">
    <svg viewBox="0 0 84 84" fill="var(--icon-ink)" stroke="var(--icon-ink)" stroke-width="6" stroke-linecap="round">
      <path d="M50 18 C72 18 72 66 50 66 Z"/>
      <path d="M38 24 H10 M38 36 H10 M38 48 H10 M38 60 H10" fill="none"/>
    </svg>
  </div>
  <div class="feature-icon icon-horn" aria-label="Horn">
    <svg viewBox="0 0 84 84" fill="var(--icon-ink)">
      <path d="M8 34 H20 L66 16 V68 L20 50 H8 Z"/>
      <rect x="66" y="20" width="10" height="44" rx="3"/>
      <rect x="22" y="52" width="10" height="16" rx="2"/>
    </svg>
  </div>
</main>
</body>
</html>
```